Podcast Graphics For Internet Business Building Podcast

We need new podcast graphics.
1400x1400
300dpi

Needs to include text "Quiet Harbor Ledger Hour" as the podcast title and "Creative Internet Income Strategies" as a subtitle.

We like blue and grey as our main colors, but are open to other schemes.

Please see attached image for an example of podcast graphics we like. While we prefer a more plain look, it would be nice to have a subtle hint related to a "machine" in the background. Something like a pencil sketch of cogs like on the Quiet Harbor Ledger 10 book cover (attached image).

Target Market(s)

online entrepreneurs or those who want to start an online business

Font styles to use
Sans Serif

Colors
0455a3
3277b5

Requirements
Must have
• Text noted in project description
Should not have
• No money symbols or flashy "make money" type things.

```html
<!DOCTYPE html>
<html lang="en">
<head>
<meta charset="utf-8">
<title>Quiet Harbor Ledger Hour — Podcast Cover</title>
<link href="https://fonts.googleapis.com/css2?family=Montserrat:wght@800&family=Oswald:wght@500&display=swap" rel="stylesheet">
<style>
  :root {
    --page-bg: #ffffff;
    --blue-deep: #0a3a80;
    --blue-mid: #0455a3;
    --blue-light: #3277b5;
    --title-white: #ffffff;
    --accent-yellow: #fccb05;
    --subtitle-ink: #4f4200;
  }
  html, body {
    margin: 0;
    padding: 0;
    width: 1177px;
    height: 1200px;
    overflow: hidden;
    background: var(--page-bg);
  }
  .canvas {
    position: relative;
    width: 1177px;
    height: 1200px;
  }
  .cover {
    position: absolute;
    left: 153px;
    top: 138px;
    width: 898px;
    height: 898px;
    overflow: hidden;
  }
  .cover-backdrop {
    position: absolute;
    inset: 0;
    width: 100%;
    height: 100%;
  }
  .title-line {
    position: absolute;
    left: 108px;
    margin: 0;
    font-family: "Montserrat", sans-serif;
    font-weight: 800;
    font-size: 124px;
    line-height: 1;
    letter-spacing: -1px;
    color: var(--title-white);
    white-space: nowrap;
  }
  .title-line--accent { color: var(--accent-yellow); }
  .line-1 { top: 175px; }
  .line-2 { top: 303px; }
  .line-3 { top: 431px; }
  .line-4 { top: 559px; }
  .subtitle-band {
    position: absolute;
    left: 113px;
    top: 690px;
    width: 782px;
    height: 62px;
    background: var(--accent-yellow);
    display: flex;
    align-items: center;
  }
  .subtitle {
    margin: 0 0 0 11px;
    font-family: "Oswald", sans-serif;
    font-weight: 500;
    font-size: 42px;
    line-height: 1;
    letter-spacing: 0.3px;
    color: var(--subtitle-ink);
    text-transform: uppercase;
    white-space: nowrap;
  }
</style>
</head>
<body>
  <div class="canvas">
    <section class="cover">
      <svg class="cover-backdrop" viewBox="0 0 898 898" role="img" aria-label="Blue blueprint background with faint grid lines and sketched machine cogs">
        <defs>
          <radialGradient id="backdropGlow" cx="0.55" cy="0.55" r="0.75">
            <stop offset="0" stop-color="#1b78c6"/>
            <stop offset="0.55" stop-color="#0e5aa8"/>
            <stop offset="1" stop-color="#0a3a80"/>
          </radialGradient>
        </defs>
        <rect width="898" height="898" fill="url(#backdropGlow)"/>
      </svg>

      <h1 class="title-line line-1">QUIET</h1>
      <p class="title-line line-2">HARBOR</p>
      <p class="title-line title-line--accent line-3">LEDGER</p>
      <p class="title-line line-4">HOUR</p>

      <div class="subtitle-band">
        <p class="subtitle">Creative Internet Income Strategies</p>
      </div>
    </section>
  </div>
</body>
</html>
```